Lone Star Wetland Flora Stewardship Guild

We need to design the home page of this new website. We would like a fun website design for provides as a resource for members and information for potential members.
Please design so that we can see a portion of background on each side on the website.
I just need the final design files psd no coding needed.
Attached is their logo (colors are not 100% set in stone either so can mess with those as I did in the quick mockup attached)
Attached is a pdf newsletter they send out, you can get a feel for them and what they are about. The design is crappy and we are here to fix that going forward and we are starting with the website.
Here are some quick example websites (design style is open)
- I attached a quick mockup i did just for a content visual but by all means do what you want.
- http://www.brindlecourtleaders.org/
- http://www.qvelto.org/
- http://preview.plimworks7.com/view.php?cat=layoutpacks&host=gridcrafthub&temp=venrolite
- http://www.ploughvale.org/
- http://www.townmarrow.org/
- http://www.projectkindlecoat.org/
here are some of the other chapters website (pretty bad!)
and here are some of the others:
- http://www.zrelkq.org/
- http://ovtu.org/
- http://www.lirvx.org/
Content Items that need to be included:
1. Logo
2. Menu - home, about, members, resources, events, membership, contact
3. Become a member - button or action
4. social links - friendwall, jobrungo, clipzora
5. banner - that needs to explain their purpose "Promoting environmental stewardship through operations, research, education and outreach" (or this can be worked into the design)
6. Upcoming event (s)
7. Advertisement - members can place an ad on the website, this can be a placeholder for now
8. newsletter signup
9. advertise with us - this link can be in the footer
30-60 years of age, succesfull (household budgets of 120K+ men and women that live in texas.
Education

```html
<!DOCTYPE html>
<html lang="en">
<head>
<meta charset="utf-8">
<title>Lone Star Wetland Flora Stewardship Guild</title>
<link rel="stylesheet" href="https://fonts.googleapis.com/css2?family=Questrial&family=Carlito:ital,wght@0,400;0,700;1,400&family=Arimo:wght@400;700&display=swap">
<style>
:root{
  --crimson:#8e1c3c;
  --crimson-light:#b04a66;
  --navy:#0b1f5b;
  --footer-navy:#06153f;
  --ink:#111;
  --grey-text:#333;
  --page-top:#d4d4d4;
}
*{box-sizing:border-box;margin:0;padding:0}
html,body{width:1200px;height:981px;overflow:hidden}
body{position:relative;background:linear-gradient(#d2d2d2 0,#e6e6e6 300px,#fff 520px,#fff);font-family:"Arimo",Arial,sans-serif;color:var(--ink)}
.abs{position:absolute}

/* top bar */
.social{top:17px;left:700px;display:flex;gap:12px;align-items:center;font:12px "Arimo",Arial,sans-serif;color:#111}
.social span{display:flex;align-items:center;gap:4px}
.social i{display:inline-block;width:10px;height:10px;border-radius:50%;background:#111}
.top-link{top:24px;font:13px "Arimo",Arial,sans-serif;color:var(--crimson);display:flex;align-items:center;gap:8px;letter-spacing:.2px}
.top-contact{left:911px}
.top-login{left:1026px}

/* brand */
.brand-wedge{left:96px;top:40px}
.brand-mark{left:104px;top:62px;font:700 58px/1 "Questrial",sans-serif;color:var(--crimson);display:flex;align-items:center;gap:10px;letter-spacing:1px}
.brand-mark i{display:inline-block;width:22px;height:22px;background:var(--navy);border-radius:50%}
.site-title{left:360px;top:64px;font:25px "Questrial",sans-serif;color:#1a1a1a;white-space:nowrap}
.title-rule{left:351px;top:102px;width:745px;height:5px;background:var(--crimson)}
.join-btn{left:912px;top:69px;width:184px;height:38px;background:linear-gradient(#b54b68,var(--crimson));color:#fff;font:17px "Questrial",sans-serif;text-align:center;line-height:36px;letter-spacing:.5px}

/* nav */
.main-nav{left:351px;top:107px;width:745px;height:51px;background:#fff;display:flex;justify-content:space-between;align-items:center;padding:0 17px;font:14.5px "Arimo",Arial,sans-serif;color:#222}

/* hero */
.hero{left:96px;top:158px;width:710px;height:334px;background:linear-gradient(160deg,#7a8f88 0%,#5e8a6e 35%,#3f6b4d 60%,#2a3b33 100%)}
.hero-caption{left:96px;top:406px;width:710px;height:86px;background:rgba(0,0,0,.72);color:#fff;font:23.5px/30px "Questrial",sans-serif;padding:12px 14px}

/* newsletter */
.newsletter{left:806px;top:158px;width:290px;height:334px;background:var(--navy);color:#fff;padding:26px 18px}
.newsletter h2{font:400 27px "Questrial",sans-serif;letter-spacing:.3px}
.newsletter p{font:14px/20px "Arimo",Arial,sans-serif;margin-top:13px}
.field{position:absolute;left:18px;width:242px;height:32px;background:#fff;color:#222;font:14px "Arimo",Arial,sans-serif;padding:8px 8px}
.field-name{top:131px}
.field-email{top:187px}
.signup-btn{position:absolute;left:130px;top:248px;width:132px;height:34px;border-radius:4px;background:linear-gradient(#fafafa,#c9c9c9);color:#222;font:21px/34px "Questrial",sans-serif;text-align:center}

/* section headers */
.band{height:53px;background:linear-gradient(#b0506b 0,#9a2c4b 40%,var(--crimson) 100%);color:#fff;font:27px/53px "Questrial",sans-serif;padding-left:16px}
.about-head{left:96px;top:532px;width:298px}
.events-head{left:439px;top:532px;width:334px}

.about-text{left:101px;top:598px;width:290px;font:15.5px/22px "Carlito",Calibri,sans-serif;color:#111}
.read-more{left:287px;top:846px;width:107px;height:27px;border-radius:4px;background:#262626;color:#fff;font:700 14px/27px "Arimo",Arial,sans-serif;text-align:center}

/* events */
.event{left:439px;width:340px;display:flex;gap:14px}
.event-thumb{width:96px;height:64px;background:linear-gradient(#8fb7dc 0,#a9c9a6 45%,#4f7a4b 70%,#6f8f6e 100%)}
.event-info{padding-top:0}
.event-title{font:700 15.5px/19px "Carlito",Calibri,sans-serif;color:var(--navy)}
.event-date{font:italic 15.5px/19px "Carlito",Calibri,sans-serif;color:var(--crimson)}
.event-text{font:15.5px/18px "Carlito",Calibri,sans-serif;color:#111;padding-left:2px}
.view-all{left:715px;top:874px;font:700 15px "Carlito",Calibri,sans-serif;color:#111}

/* ad */
.ad-visual{left:821px;top:532px;width:274px;height:286px;background:radial-gradient(circle at 60% 40%,#3a8bc4,#12507f 70%,#0c3556)}
.ad-foot{left:821px;top:818px;width:274px;height:77px;background:#d7d7d7}

/* footer */
.site-footer{left:0;top:926px;width:1200px;height:55px;background:var(--footer-navy);color:#d0d4e0}
.copyright{position:absolute;left:103px;top:14px;font:14.5px "Arimo",Arial,sans-serif}
.advertise{position:absolute;left:964px;top:13px;font:16.5px "Arimo",Arial,sans-serif;text-decoration:underline;color:#d0d4e0}
</style>
</head>
<body>

<div class="abs social">
  <span><i></i>friendwall</span>
  <span><i></i>jobrungo</span>
  <span><i></i>clipzora</span>
</div>
<div class="abs top-link top-contact">CONTACT
  <svg width="20" height="14" viewBox="0 0 20 14"><rect x="0.5" y="0.5" width="19" height="13" fill="#111"/><path d="M1 1l9 7 9-7" stroke="#fff" stroke-width="1.4" fill="none"/></svg>
</div>
<div class="abs top-link top-login">LOGIN
  <svg width="20" height="20" viewBox="0 0 20 20"><g fill="#444"><circle cx="10" cy="10" r="6.5"/><rect x="8.3" y="0.5" width="3.4" height="19"/><rect x="0.5" y="8.3" width="19" height="3.4"/><rect x="8.3" y="0.5" width="3.4" height="19" transform="rotate(45 10 10)"/><rect x="8.3" y="0.5" width="3.4" height="19" transform="rotate(-45 10 10)"/></g><circle cx="10" cy="10" r="2.8" fill="#ddd"/></svg>
</div>

<svg class="abs brand-wedge" width="260" height="118" viewBox="0 0 260 118"><path d="M150 118 C190 90 220 70 255 62 L255 118 Z" fill="#fff"/></svg>
<div class="abs brand-mark"><i></i>LSWG</div>
<div class="abs site-title">Lone Star Wetland Flora Stewardship Guild</div>
<div class="abs title-rule"></div>
<div class="abs join-btn">BECOME A MEMBER</div>

<nav class="abs main-nav">
  <span>HOME</span><span>ABOUT</span><span>MEMBERS</span><span>RESOURCES</span><span>EVENTS</span><span>MEMBERSHIP</span><span>CONTACT</span>
</nav>

<div class="abs hero" role="img" aria-label="Photo of water lilies and reeds on a calm pond with a white lily flower"></div>
<div class="abs hero-caption">Promoting environmental stewardship through operations,<br>research, education and outreach</div>

<section class="abs newsletter">
  <h2>Newsletter Sign Up</h2>
  <p>Neque porro quisquam est qui dolorem ipsum quia dolor sit amet, consectetur</p>
  <div class="field field-name">Your Name</div>
  <div class="field field-email">Email Address</div>
  <div class="signup-btn">Sign Up</div>
</section>

<div class="abs band about-head">About LSWG</div>
<p class="abs about-text">The Lone Star Wetland Flora Stewardship Guild, Inc. is an organization of scientists, educators, students, commercial pesticide applicators, administrators, and concerned individuals interested in the management and study of aquatic plants. The membership reflects a diversity of federal, state, and local agencies; universities and colleges around the world; corporations; and small businesses.</p>
<div class="abs read-more">Read More</div>

<div class="abs band events-head">Upcoming Events</div>
<div class="abs event" style="top:602px">
  <div class="event-thumb" role="img" aria-label="Photo of a pond with lily pads"></div>
  <div class="event-info"><div class="event-title">2014 Northeast Aquatic Plant</div><div class="event-date">January 21, 2014</div><div class="event-text">Lorem Ipsum is simply dummy text<br>of the printing .</div></div>
</div>
<div class="abs event" style="top:694px">
  <div class="event-thumb" role="img" aria-label="Photo of a reedy pond edge"></div>
  <div class="event-info"><div class="event-title">2014 Northeast Aquatic Plant</div><div class="event-date">January 21, 2014</div><div class="event-text">Lorem Ipsum is simply dummy text<br>of the printing .</div></div>
</div>
<div class="abs event" style="top:789px">
  <div class="event-thumb" role="img" aria-label="Photo of a pond with lily pads"></div>
  <div class="event-info"><div class="event-title">2014 Northeast Aquatic Plant</div><div class="event-date">January 21, 2014</div><div class="event-text">Lorem Ipsum is simply dummy text<br>of the printing .</div></div>
</div>
<div class="abs view-all">View All..</div>

<div class="abs ad-visual" role="img" aria-label="Advertisement photo of ClearPond Pro algaecide jug and bag on blue water"></div>
<div class="abs ad-foot" role="img" aria-label="Advertiser brand area for Marshwell Labs"></div>

<footer class="abs site-footer">
  <span class="copyright">Copyright © 2014 LSWG. All rights reserved.</span>
  <span class="advertise">advertise with us</span>
</footer>

</body>
</html>
```